Sandalwood Apartments —-

Letter head for my apartment building of 15 Floors
In Kampala, Uganda

SANDALWOOD APARTMENTS
47 MBERIVO CREST ROAD
NAGURU - KAMPALA
P.O. BOX 58316
KAMPALA— UGANDA

```html
<!DOCTYPE html>
<html lang="en">
<head>
<meta charset="utf-8">
<title>Sandalwood Apartments — Letterhead</title>
<link rel="stylesheet" href="https://fonts.googleapis.com/css2?family=Work+Sans:wght@400;500;700&display=swap">
<style>
  :root {
    --backdrop: #e4e4e6;
    --paper: #ffffff;
    --brand-blue: #1170b7;
    --swoosh-grey: #4a4a4c;
    --ink: #1f1f22;
    --muted: #6d6d72;
  }
  * { box-sizing: border-box; margin: 0; padding: 0; }
  html, body {
    width: 1200px; height: 898px; overflow: hidden;
    background: var(--backdrop);
    font-family: "Work Sans", sans-serif;
  }
  .letterhead {
    position: absolute; left: 300px; top: 25px;
    width: 600px; height: 848px;
    background: var(--paper);
    box-shadow: 0 6px 24px rgba(0,0,0,0.12);
    overflow: hidden;
  }
  .masthead { position: absolute; top: 72px; left: 0; right: 0; text-align: center; }
  .masthead__name {
    color: var(--brand-blue); font-weight: 700;
    font-size: 22px; letter-spacing: 2.2px;
  }
  .masthead__address {
    color: var(--muted); font-size: 9px; letter-spacing: 2.2px; margin-top: 1px;
  }
  .masthead__rule {
    position: absolute; top: 124px; left: 30px; right: 0;
    height: 2px; background: var(--brand-blue);
  }
  .letter-body {
    position: absolute; top: 196px; left: 110px;
    color: var(--ink); font-size: 10.5px; line-height: 15px;
    letter-spacing: 0.4px;
  }
  .salutation { font-size: 12px; font-weight: 500; line-height: 13px; }
  .salutation__title { display: block; font-size: 9px; color: var(--muted); margin-left: 4px; line-height: 10px; }
  .letter-body p { white-space: nowrap; margin-left: 22px; margin-bottom: 15px; }
  .letter-body p .indent { display: inline-block; width: 50px; }
  .letter-body p.tight { margin-bottom: 0; }
  .contact {
    position: absolute; top: 664px; right: 62px;
    text-align: right; color: var(--muted);
    font-size: 9.5px; line-height: 13px; letter-spacing: 0.6px;
  }
  .contact__row { display: flex; justify-content: flex-end; align-items: center; gap: 5px; }
  .contact__row svg { width: 8px; height: 8px; fill: var(--brand-blue); }
  .street-address {
    position: absolute; top: 728px; left: 150px;
    color: var(--muted); font-size: 9px; line-height: 12px; letter-spacing: 1.2px;
  }
  .footer-band { position: absolute; left: 0; bottom: 0; width: 600px; height: 100px; }
</style>
</head>
<body>
  <main class="letterhead">
    <header class="masthead">
      <h1 class="masthead__name">SANDALWOOD APARTMENTS</h1>
      <p class="masthead__address">P.O. BOX 58316 KAMPALA— UGANDA</p>
    </header>
    <div class="masthead__rule"></div>

    <section class="letter-body">
      <div class="salutation">Dear<span class="salutation__title">Sir</span></div>
      <p><span class="indent"></span>Lorem ipsum dolor sit amet, consectetuer adipiscing elit,<br>sed diam nonummy nibh euismod tincidunt ut laoreet dolore<br>magna aliquam erat volutpat. Ut wisi enim ad minim veniam, quis<br>nostrud exerci tation ullamcorper suscipit lobortis nisl ut aliquip<br>ex ea commodo consequat. Duis autem vel eum iriure dolor in<br>hendrerit in vulputate velit esse molestie consequat, vel illum<br>dolore eu feugiat nulla facilisis at vero eros et accumsan et iusto<br>odio dignissim qui blandit praesent luptatum zzril delenit augue<br>duis dolore te feugait nulla facilisi.</p>
      <p class="tight"><span class="indent"></span>Lorem ipsum dolor sit amet, cons ectetuer adipiscing elit,<br>sed diam nonummy nibh euismod tincidunt ut laoreet dolore<br>magna aliquam erat volutpat. Ut wisi enim ad minim veniam, quis<br>nostrud exerci tation ullamcorper suscipit lobortis nisl ut aliquip<br>ex ea commodo consequat.</p>
      <p><span class="indent"></span>Lorem ipsum dolor sit amet, consectetuer adipiscing elit,<br>sed diam nonummy nibh euismod tincidunt ut laoreet dolore<br>magna aliquam erat volutpat. Ut wisi enim ad minim veniam, quis<br>nostrud exerci tation ullamcorper suscipit lobortis nisl ut aliquip<br>ex ea commodo consequat. Duis autem vel eum iriure dolor in<br>hendrerit in vulputate velit esse molestie consequat, vel illum<br>dolore eu feugiat nulla facilisis at vero eros et accumsan et iusto<br>odio dignissim qui blandit praesent luptatum zzril delenit augue<br>duis dolore te feugait nulla facilisi.</p>
      <p class="tight"><span class="indent"></span>Lorem ipsum dolor sit amet, cons ectetuer adipiscing elit,<br>sed diam nonummy nibh euismod tincidunt ut laoreet dolore</p>
    </section>

    <address class="contact" style="font-style:normal">
      <div class="contact__row">(256) 414-7302
        <svg viewBox="0 0 10 10"><path d="M2 0.5 L3.6 2.6 L2.8 3.6 Q4 6 6.4 7.2 L7.4 6.4 L9.5 8 L8.4 9.5 Q3.5 9 0.5 1.6 Z"/></svg></div>
      <div class="contact__row">info@sandalwoodapts.com
        <svg viewBox="0 0 10 10"><path d="M0.5 2 H9.5 V8 H0.5 Z M1.4 2.8 V7.2 H8.6 V2.8 L5 5.4 Z" fill-rule="evenodd"/></svg></div>
      <div class="contact__row">www.sandalwoodapts.com
        <svg viewBox="0 0 10 10"><circle cx="5" cy="5" r="4.5"/></svg></div>
    </address>

    <address class="street-address" style="font-style:normal">
      47 MBERIVO CREST ROAD<br>NAGURU - KAMPALA
    </address>

    <svg class="footer-band" viewBox="0 0 600 100" preserveAspectRatio="none" aria-hidden="true">
      <path d="M0 28 C140 52 320 60 600 62 L600 100 L0 100 Z" fill="var(--brand-blue)"/>
      <path d="M170 40 C330 46 480 50 600 44 L600 53 C480 58 330 52 170 40 Z" fill="var(--swoosh-grey)"/>
    </svg>
  </main>
</body>
</html>
```